kleines Übersetzungsbüro sucht Design für Folder
Zielgruppe
Als Selbständige betreibe ich ein Italienisch-Übersetzungsbüro, das mit qualitativ hochwertigen Übersetzungen und maßgeschneidertem Service wirbt. Meine Tätigkeiten drehen sich um die Fachbereiche Recht und PR/Marketing/Corporate Communication.
Aufgabenstellung
Die Broschüre soll dynamisch,frisch, luftig, aber professionell wirken und gerne an den Stil meiner Website angelehnt sein.
Eine leicht minimalistische Gestaltung mit farbigen Akzenten (z.B. grafische Elemente) ist durchaus willkommen, aber nicht zwingend. Wenn das Endergebnis stimmig und überzeugend ist, lasse ich mich gerne umstimmen.
Auf das genaue Format des Folders möchte ich mich nicht festlegen. Ob einfach gefalzt, mit Wickel- oder Z-Falz: die Wahl überlasse ich Ihnen.
Der Folder soll zunächst nur per Mail übermittelt bzw. online verfügbar sein. Es empfiehlt sich also ein Format, bei dem die Inhalte überschaubar dargestellt sind und auf einen Blick erfasst werden können.
Alle CI-Farben sollten bei der Gestaltung berücksichtigt werden.
Vorgaben für die Verwendung vom Bildmaterial siehe hochgeladenes Briefingdokument.
Die Broschüre soll die Botschaft vermitteln, dass es sich lohnt auf einen dynamischen, zuverlässigen Profi zu setzen, der für einen immer da ist und pfiffige Leistungen erbringt.

```html
<!DOCTYPE html>
<html lang="de">
<head>
<meta charset="utf-8">
<title>linguaviva – Folder</title>
<link href="https://fonts.googleapis.com/css2?family=Fira+Sans+Condensed:wght@300;400&display=swap" rel="stylesheet">
<style>
:root{
  --bg:#000;
  --paper:#fff;
  --lime:#b9dc12;
  --green:#5dad18;
  --text:#5a5a5a;
  --label:#9a9a9a;
  --photo-office-a:#dfe8ee;
  --photo-office-b:#8fa6b8;
  --photo-desk-a:#f2f2f0;
  --photo-desk-b:#c9cdc6;
  --photo-portrait-a:#e9dcd2;
  --photo-portrait-b:#3f9a4a;
}
*{margin:0;padding:0;box-sizing:border-box}
html,body{width:1200px;height:848px;overflow:hidden;background:var(--bg)}
body{font-family:"Fira Sans Condensed",Arial,sans-serif;color:var(--text);position:relative}
.side-label{position:absolute;color:var(--label);font-weight:300;font-size:15px;letter-spacing:.3px}
.spread{position:absolute;top:240px;width:570px;height:403px;background:var(--paper);overflow:hidden}
.spread--front{left:15px}
.spread--back{left:615px}
.spread svg.art{position:absolute;inset:0}
.panel{position:absolute;top:0;width:190px;height:403px}
.panel h2{color:var(--green);font-weight:400;font-size:10px;line-height:1.05;margin-bottom:5px}
.panel p,.panel li{font-size:4.6px;line-height:1.35;font-weight:300}
.panel p{margin-bottom:4px}
.panel ul{list-style:none;margin-bottom:4px}
.fold{position:absolute;top:0;width:6px;height:403px;background:linear-gradient(90deg,rgba(0,0,0,.07),rgba(0,0,0,0))}
.brand{color:var(--green);font-size:15px;font-weight:400;text-align:center;display:flex;align-items:center;justify-content:center;gap:5px}
.brand-dot{width:9px;height:9px;border-radius:50%;background:var(--green)}
.tagline{color:var(--green);font-size:8.5px;text-align:center;line-height:1.25;margin-top:6px}
.contact{font-size:4.8px;text-align:center;line-height:1.4;margin-top:12px}
.cols{display:flex;gap:26px}
</style>
</head>
<body>

<div class="side-label" style="left:43px;top:210px">front side</div>
<div class="side-label" style="left:178px;top:212px">page4</div>
<div class="side-label" style="left:326px;top:212px">page5</div>
<div class="side-label" style="left:467px;top:212px">COVER</div>
<div class="side-label" style="left:713px;top:212px">page1</div>
<div class="side-label" style="left:845px;top:212px">page2</div>
<div class="side-label" style="left:989px;top:212px">page3</div>
<div class="side-label" style="left:1098px;top:185px">back side</div>

<!-- Außenseite -->
<section class="spread spread--front">
  <svg class="art" width="570" height="403" viewBox="0 0 570 403">
    <defs>
      <linearGradient id="gOffice" x1="0" y1="0" x2="1" y2="1">
        <stop offset="0" stop-color="var(--photo-office-a)"/><stop offset="1" stop-color="var(--photo-office-b)"/>
      </linearGradient>
      <clipPath id="cP4"><rect x="0" y="0" width="190" height="403"/></clipPath>
      <clipPath id="cCover"><rect x="380" y="0" width="190" height="403"/></clipPath>
    </defs>
    <g clip-path="url(#cP4)">
      <g role="img" aria-label="Foto: Mann im blauen Hemd bei einer Besprechung im Büro">
        <ellipse cx="88" cy="300" rx="112" ry="56" fill="url(#gOffice)"/>
      </g>
      <path d="M-10 225 C 120 225 205 262 188 320 C 176 360 90 365 -10 355" fill="none" stroke="var(--lime)" stroke-width="9"/>
      <path d="M-10 360 C 80 372 170 362 192 330" fill="none" stroke="var(--green)" stroke-width="6"/>
    </g>
    <g clip-path="url(#cCover)">
      <g role="img" aria-label="Foto: Geschäftsleute im hellen Büro, Diagramme und Stift auf dem Tisch">
        <ellipse cx="500" cy="140" rx="118" ry="128" fill="url(#gOffice)"/>
      </g>
      <path d="M560 0 C 440 10 378 90 386 170 C 395 240 470 270 575 262" fill="none" stroke="var(--green)" stroke-width="11"/>
      <path d="M470 -5 C 520 5 560 10 580 25" fill="none" stroke="var(--lime)" stroke-width="12"/>
    </g>
  </svg>
  <div class="fold" style="left:190px"></div>
  <div class="fold" style="left:380px"></div>

  <div class="panel" style="left:0;padding:24px 18px 0 22px">
    <h2>Einige Highlights aus<br>meinem Portfolio</h2>
    <p>Speziell für juristische Texte wie: Verträge, AGB, Klagen, Urteile, Urkunden, Beschlüsse, Protokolle, Registerauszüge, Satzungen und Schriftsätze.</p>
    <ul><li>- Übersetzungen</li><li>- Beglaubigungen</li><li>- Einholung von Apostillen</li><li>- 4- und 6-Augenkontrolle</li><li>- Express-Service</li></ul>
    <p>Speziell für PR- und Marketingtexte wie: Pressemitteilungen, Websites, Newsletter, Mitarbeitermagazine, Unternehmensberichte, Kampagnen, Markt- und Organisationskommunikation sowie Social Networks.</p>
    <ul><li>- Übersetzung, Adaption und Transkreation</li><li>- Briefing im Vorfeld der Projektumsetzung</li><li>- Erstellung kundenspezifischer Terminologie</li><li>- 4- und 6-Augenkontrolle</li><li>- Gut-zum-Druck</li></ul>
  </div>

  <div class="panel" style="left:190px;padding:20px 16px 0 18px">
    <h2>Ihr direkter Draht zum<br>Übersetzungsprofi</h2>
    <p>Wenn Sie eine Agentur beauftragen, haben Sie zwar einen direkten Ansprechpartner, doch der übersetzt meist nicht selbst. Er gibt Ihren Auftrag weiter und oft erfahren Sie nie, wer tatsächlich an Ihrem Text arbeitet. Bei mir wissen Sie immer, mit wem Sie es zu tun haben. Ich bin Ihre unmittelbare Ansprechpartnerin, kenne Ihre Wünsche von Anfang an und begleite jede Phase des Auftrags persönlich. Auf dem kleinen Dienstweg entsteht eine effiziente und passgenaue Zusammenarbeit – genau das, was Sie benötigen!</p>
    <h2 style="margin-top:7px">Ihre Investition in Qualität</h2>
    <p>Agenturen haben einen hohen Verwaltungsaufwand und verlangen dafür ein beachtliches Honorar, von dem der Übersetzer am Ende nur einen kleinen Teil erhält. Wer selbst einen angemessenen Preis für seine Arbeit zahlen möchte, erwartet echte Qualität statt Dumping-Preis. Investieren Sie daher lieber direkt in das Endprodukt – ohne zwischengeschaltete Vermittler und ohne versteckte Kosten. Bei mir fließt jeder Cent garantiert in Qualitätsarbeit!</p>
    <h2 style="margin-top:7px">Meine Werte – Ihr Mehrwert</h2>
    <p>Meine Werte sind Ihr garantierter Mehrwert. Sie müssen keine Umwege über Vermittlungsbüros gehen, sondern erteilen Ihren Auftrag direkt an mich. Ich stehe Ihnen als persönliche Ansprechpartnerin zur Verfügung – auch in Zeiten, in denen Büros längst Feierabend haben. Dank kurzer Wege erreichen Sie mich jederzeit per Mail oder Telefon, auch wenn es einmal eilig ist. Bei aller Unkompliziertheit stehen Professionalität, Diskretion und Termintreue an erster Stelle. Ich biete Ihnen maximale Transparenz bei Preisgestaltung und Projektablauf.</p>
    <p>Setzen Sie daher auf:</p>
    <div class="cols">
      <ul><li>-Professionalität</li><li>-Transparenz</li><li>-kurze Wege</li></ul>
      <ul><li>-persönliche Beziehungen</li><li>-kompromisslose Qualität</li></ul>
    </div>
  </div>

  <div class="panel" style="left:380px;padding:268px 10px 0 10px">
    <div class="brand"><span class="brand-dot"></span>linguaviva</div>
    <div class="tagline">Italienisch-Übersetzungen<br>mit Pfiff – direkt vom Profi</div>
    <div class="contact">linguaviva<br>Inh.: Chiara Fontana<br>Lindenweg 7<br>54290 Trier<br>Tel.: 0651 4471023<br>Mobil: 0170 5528391<br>Web: www.linguaviva-studio.de<br>Mail: info@linguaviva-studio.de</div>
  </div>
</section>

<!-- Innenseite -->
<section class="spread spread--back">
  <svg class="art" width="570" height="403" viewBox="0 0 570 403">
    <defs>
      <linearGradient id="gDesk" x1="0" y1="0" x2="1" y2="1">
        <stop offset="0" stop-color="var(--photo-desk-a)"/><stop offset="1" stop-color="var(--photo-desk-b)"/>
      </linearGradient>
      <linearGradient id="gOffice2" x1="0" y1="0" x2="1" y2="1">
        <stop offset="0" stop-color="var(--photo-office-a)"/><stop offset="1" stop-color="var(--photo-office-b)"/>
      </linearGradient>
      <linearGradient id="gPortrait" x1="0" y1="0" x2="0" y2="1">
        <stop offset="0" stop-color="var(--photo-portrait-a)"/><stop offset="1" stop-color="var(--photo-portrait-b)"/>
      </linearGradient>
      <clipPath id="cP2"><rect x="190" y="0" width="190" height="403"/></clipPath>
      <clipPath id="cP3"><rect x="380" y="0" width="190" height="403"/></clipPath>
    </defs>
    <g role="img" aria-label="Foto: Schreibtisch von oben mit Pflanze, Notizblock, Stiften, Kaffeetasse und Tastatur">
      <rect x="0" y="0" width="380" height="92" fill="url(#gDesk)"/>
    </g>
    <g clip-path="url(#cP2)">
      <g role="img" aria-label="Porträtfoto der Übersetzerin in grünem Oberteil">
        <ellipse cx="305" cy="335" rx="95" ry="88" fill="url(#gPortrait)"/>
      </g>
      <path d="M380 245 C 300 250 215 290 215 350 C 215 390 260 403 300 410" fill="none" stroke="var(--green)" stroke-width="9"/>
    </g>
    <path d="M0 340 C 90 385 200 400 380 375 C 430 368 500 350 580 318" fill="none" stroke="var(--lime)" stroke-width="12"/>
    <path d="M0 372 C 120 410 260 408 380 392" fill="none" stroke="var(--green)" stroke-width="5"/>
    <g clip-path="url(#cP3)">
      <g role="img" aria-label="Foto: Geschäftsleute im Büro vor einer Präsentation mit Diagramm">
        <ellipse cx="500" cy="85" rx="102" ry="72" fill="url(#gOffice2)"/>
      </g>
      <path d="M575 12 C 470 -5 395 30 395 85 C 395 140 480 160 575 140" fill="none" stroke="var(--green)" stroke-width="10"/>
    </g>
  </svg>
  <div class="fold" style="left:190px"></div>
  <div class="fold" style="left:380px"></div>

  <div class="panel" style="left:0;padding:104px 14px 0 16px">
    <h2>Wenn Großes im<br>Kleinen entsteht</h2>
    <p>Qualität war schon immer eine Frage des Könnens – das gilt insbesondere auch für den Übersetzungsbereich. Deshalb überzeugt mein Büro seit über 13 Jahren private Kunden, Behörden und Unternehmen der freien Wirtschaft mit einem hochprofessionellen Übersetzungsservice, der keine Wünsche offen lässt. Frei nach dem Motto „Klein, aber fein“.</p>
    <p>Vielleicht kann ich bald auch Sie überzeugen. Unterhalten Sie Geschäftsbeziehungen nach Italien? Planen Sie Marketingaktionen oder PR-Kampagnen für Ihre Zielgruppen im italienischen Sprachraum? Dann bin ich</p>
    <h2 style="margin-top:6px">Ihre Ansprechpartnerin und Wegbegleiterin für Italienisch-Fachübersetzungen.</h2>
    <ul><li>Chiara Fontana</li><li>Dottoressa in Traduzione</li><li>Italienisch Deutsch Englisch</li><li>Allg. beeid. Übersetzerin und Dolmetscherin</li><li>Mitglied im Fachverband für Sprachmittler</li><li>Übersetzerin</li><li>Korrektorin</li><li>Transkreative Texterin</li></ul>
  </div>

  <div class="panel" style="left:190px;padding:96px 14px 0 14px">
    <p>Als italienische Muttersprachlerin verfüge ich über jene fundierte Sprachkenntnis und -sensibilität, die für Ihre Fachtexte unentbehrlich ist. Seit mehr als einem Jahrzehnt bin ich als selbstständige Übersetzerin für anspruchsvolle Fachtexte tätig. Meine akademische Ausbildung ergänze ich durch regelmäßige Weiterbildung, um stets auf dem neuesten Stand zu bleiben, etwa in puncto Fachwissen, Allgemeinbildung und Sprachpflege. Moderne Übersetzungswerkzeuge unterstützen mich dabei, Terminologie und Stil konsistent zu halten. Meine Talente wie große Sprachgewandtheit, Kreativität und Feingefühl bringe ich mit auf die Waage, damit Sie am Ende eine perfekte Übersetzung in den Händen halten.</p>
    <p>Juristische Übersetzungen und Übersetzungen im Bereich Marketing und PR – auf diese beiden Schwerpunkte habe ich mich spezialisiert. Erstere bedürfen absoluter Präzision. Gerade juristische Texte müssen eindeutig und genau formuliert werden, denn selbst kleinste Ungenauigkeiten können große Schäden nach sich ziehen. Hier sollten Sie nichts dem Zufall überlassen, da nicht nur Texte übersetzt werden, sondern auch die Besonderheiten zweier Rechtssysteme berücksichtigt werden müssen.</p>
  </div>

  <div class="panel" style="left:380px;padding:168px 16px 0 16px">
    <p>Dank meiner einschlägigen Berufserfahrung verfüge ich über solide juristische Kenntnisse und garantiere Ihnen die strikte Einhaltung der Prinzipien der Rechtsübersetzung. Diskretion versteht sich von selbst. So sind Sie auf der sicheren Seite!</p>
    <p>Übersetzungen für Marketing und Public Relations sind hingegen deutlich vielschichtiger. Hier geht es nicht um wortgenaue Übersetzungen, sondern darum, eine Zielgruppe mit einem anderen sprachlichen und kulturellen Hintergrund zu erreichen und zu bewegen. Dazu brauchen Sie die griffigen, knackigen und zielsprachlich authentischen Übersetzungen einer Spezialistin für Adaption und Transkreation. Mit meiner ausgeprägten interkulturellen Sensibilität, textlichen Kreativität und meinem Repertoire an Schreibtechniken gelingt mir der Spagat zwischen Sprachen und Kulturen. Gemeinsam steigern wir die Attraktivität Ihres Images bei Ihrer Zielgruppe in Italien und im Tessin.</p>
  </div>
</section>

</body>
</html>
```